Simple Business Cards for Self-employed Coach

Simple business card with a design that includes the QLT logo.
Using either only the logo color or additional colors that match the logo.

Meridian Guides reach deeply into the past, gathering wisdom from East and West, while still staying current with the frontiers of new discovery in cognitive science, genetics, and other disciplines. see https://www.brightharborpath.example/what-is-integral-coaching/

Target Market(s)

Coaching Clients in Tokyo /Asia; in business organizations, but also outside

Industry/Entity Type

Life Coaching

Contact Information for Business Card

Lukas Brenning
Certified Meridian Guide

3-2-48 Kamiyoshi
Nakarino 164-0392
Tokyo, Japan

Phone: +81 70 4817 5062
E-Mail: lukas.brenning@mailora.example

Font styles to use
Sans Serif

Colors
00a990

Requirements
Must have
• include uploaded logo
• color fitting with QLT logo color
Nice to have
• simple, elegant design
Should not have
• clutter

```html
<!DOCTYPE html>
<html lang="en">
<head>
<meta charset="utf-8">
<title>Lukas Brenning – Business Card</title>
<link rel="stylesheet" href="https://fonts.googleapis.com/css2?family=Open+Sans:wght@400;700&display=swap">
<style>
  :root {
    --teal: #00a990;
    --teal-deep: #078f7f;
    --teal-soft: #1fb3a0;
    --ink: #1a1a1a;
    --paper: #ffffff;
    --backdrop: #e9e7e3;
  }
  html, body {
    margin: 0;
    width: 1200px;
    height: 902px;
    overflow: hidden;
    background: var(--backdrop);
  }
  .business-card {
    position: absolute;
    left: 75px;
    top: 151px;
    width: 1050px;
    height: 600px;
    background: var(--paper);
    box-shadow: 0 6px 24px rgba(0,0,0,0.18);
    font-family: "Open Sans", sans-serif;
    overflow: hidden;
  }
  .block {
    position: absolute;
    background: linear-gradient(135deg, var(--teal-deep), var(--teal-soft));
  }
  .block--upper { left: 0; top: 300px; width: 330px; height: 170px; }
  .block--lower { left: 420px; top: 390px; width: 300px; height: 170px; }
  .brand {
    position: absolute;
    left: 150px;
    top: 490px;
    display: flex;
    align-items: center;
    gap: 12px;
  }
  .brand__square {
    width: 26px;
    height: 26px;
    border: 3px solid var(--teal);
    box-sizing: border-box;
  }
  .brand__name {
    font-weight: 700;
    font-size: 40px;
    color: var(--teal);
    line-height: 1;
  }
  .contact {
    position: absolute;
    right: 60px;
    top: 55px;
    text-align: right;
    color: var(--ink);
  }
  .contact__name {
    margin: 0;
    font-size: 40px;
    font-weight: 700;
    letter-spacing: 0.5px;
    line-height: 1.1;
    text-transform: uppercase;
  }
  .contact__surname { color: var(--teal); }
  .contact__title {
    margin: 2px 0 0;
    font-size: 21px;
  }
  .rule {
    position: absolute;
    right: 40px;
    top: 155px;
    width: 540px;
    height: 4px;
    background: var(--teal);
  }
  .rule::after {
    content: "";
    position: absolute;
    right: -4px;
    top: -36px;
    width: 4px;
    height: 24px;
    background: var(--teal);
  }
  .details {
    position: absolute;
    right: 60px;
    top: 180px;
    text-align: right;
    font-size: 21px;
    font-style: normal;
    line-height: 1.7;
    color: var(--ink);
  }
  .details p { margin: 0; }
  .details .gap { margin-top: 12px; }
  .details .value { color: var(--teal); }
  .edge-tick {
    position: absolute;
    left: 0;
    top: 540px;
    width: 16px;
    height: 3px;
    background: var(--teal);
  }
</style>
</head>
<body>
  <section class="business-card">
    <div class="block block--upper"></div>
    <div class="block block--lower"></div>
    <div class="edge-tick"></div>

    <div class="brand">
      <span class="brand__square"></span>
      <span class="brand__name">QLT</span>
    </div>

    <header class="contact">
      <h1 class="contact__name">Lukas<span class="contact__surname">Brenning</span></h1>
      <p class="contact__title">Certified Meridian Guide</p>
    </header>
    <div class="rule"></div>

    <address class="details">
      <p>3-2-48 Kamiyoshi</p>
      <p>Nakarino 164-0392 Tokyo, Japan</p>
      <p class="gap">P: <span class="value">+81 70 4817 5062</span></p>
      <p>E: <span class="value">lukas.brenning@mailora.example</span></p>
    </address>
  </section>
</body>
</html>
```